Update Website, Include new Logo

We are a Technology Managed Service Provider (MSP)
+cyber security company operating out of New York City and New Jersey. Our main customer base has been financial service industry, high tech, multi-media, and/or other enterprise level customers. Current website is very old but still valid from an offering standpoint but we now want to emphasize and focus more on Cyber Security. We are offering a new cybersecurity line targeted at offering NGOs, Government, and Small-Mid Sized businesses the same level of cybersecurity as big business.

We would like to incorporate the new Varlowe logo and keep the feel modern, secure (without feeling aggressive). We want our clients to feel we will offer them white glove service at affordable cost - safety, security and stability are attainable at all levels.

I am attaching logos for visual, as you need copy, please let us know and we can send you the verbiage. Our current site is www.varlowe-example.com for comparison

Target Market(s)

Any businesses who need cyber security

Industry/Entity Type

Technology - Cybersecurity

Number of Pages Required

3 page

Colors
0054AA
0677BA
7BADD7
CADEEF
E8F1F8
FFC000
F8CF3A
FAE287
FDF2CF
FEFAEE
F0912C
F2A743
F7CA91
FBE8D2
FDF5EE
EE7325
F08F49
F5BC92
FAE3D3
FDF4ED

Requirements
Must have
• Bulleted points about SOC, compliance, Pellorin, etc (see marketing doc). Please use the new Varlowe Logo (in zip), we like the orange version (with the fading color). Would like to have that color be included throughout, however do not want it to be childish. Open to ideas on colors/layout/imagery
Nice to have
• An area to capture customer data (schedule a Penetration Test, ask for more info, or check pricing), or a link/qr code area we can add that
Should not have
• Halloween feel, An aggressive feel, hard sell. Not large areas of paragraphs (like our current page).

```html
<!DOCTYPE html>
<html lang="en">
<head>
<meta charset="utf-8">
<title>Varlowe Technology — Enterprise-Level Cybersecurity</title>
<link href="https://fonts.googleapis.com/css2?family=Outfit:wght@500;600;700&family=Poppins:wght@400;500;600;700&display=swap" rel="stylesheet">
<style>
:root{
  --orange:#EE7325;
  --orange-mid:#F0912C;
  --amber:#FFC000;
  --amber-soft:#F8CF3A;
  --peach:#FDF4ED;
  --peach-mid:#FBE8D2;
  --ink:#111111;
  --dark:#161616;
  --grey:#bdbdbd;
  --text:#333333;
  --line:#9a9a9a;
  --white:#ffffff;
}
*{box-sizing:border-box;margin:0;padding:0}
html,body{width:1200px;height:3495px;overflow:hidden}
body{position:relative;font-family:"Poppins",sans-serif;color:var(--text);background:var(--white)}
.abs{position:absolute}
h1,h2,h3,.brand-name{font-family:"Outfit",sans-serif}
.accent{color:var(--orange-mid);background:linear-gradient(90deg,var(--orange),var(--amber));-webkit-background-clip:text;background-clip:text;color:transparent}

/* header */
.site-header{left:0;top:0;width:1200px;height:77px;background:var(--white);z-index:5}
.brand{left:112px;top:14px;display:flex;align-items:center;gap:10px}
.brand-dot{width:44px;height:44px;border-radius:50%;background:linear-gradient(135deg,var(--orange),var(--amber))}
.brand-name{font-size:31px;font-weight:700;color:var(--ink);line-height:1;letter-spacing:.5px}
.brand-sub{font-family:"Poppins",sans-serif;font-size:10px;letter-spacing:4px;color:#999;margin-left:30px;display:block;margin-top:2px}
.main-nav{top:0;left:445px;height:77px;display:flex;align-items:center;gap:36px;font-size:11px;font-weight:600;color:var(--ink)}
.main-nav a{color:inherit;text-decoration:none;position:relative;height:77px;line-height:77px}
.main-nav a.active{color:var(--orange)}
.main-nav a.active::after{content:"";position:absolute;left:0;right:0;bottom:0;height:3px;background:var(--orange)}
.search-icon{left:900px;top:29px}
.btn-touch{left:944px;top:19px;width:142px;height:40px;clip-path:polygon(8% 0,92% 0,100% 50%,92% 100%,8% 100%,0 50%);background:linear-gradient(90deg,var(--orange),var(--amber));color:var(--white);font-size:11px;font-weight:700;display:flex;align-items:center;justify-content:center}

/* hero */
.hero{left:0;top:77px;width:1200px;height:760px;clip-path:polygon(0 0,100% 0,100% 528px,0 752px);background:radial-gradient(ellipse 380px 420px at 880px 300px,rgba(240,145,44,.55),rgba(255,192,0,.15) 55%,transparent 75%),radial-gradient(circle at 850px 200px,#555 0,#222 40%,#0c0c0c 80%)}
.hero-kicker{left:115px;top:250px;font-size:15px;font-weight:500;color:var(--white)}
.hero-title{left:113px;top:282px;font-size:48px;font-weight:700;line-height:56px;color:var(--white)}
.hero-text{left:114px;top:469px;font-size:12.5px;line-height:19px;color:var(--white)}
.btn-light{left:115px;top:533px;width:256px;height:40px;clip-path:polygon(6% 0,94% 0,100% 50%,94% 100%,6% 100%,0 50%);background:var(--white);color:var(--ink);font-size:11px;font-weight:700;display:flex;align-items:center;justify-content:center}

/* gap section */
.glow-left{left:0;top:800px;width:520px;height:520px;background:radial-gradient(circle at 0 30%,var(--peach-mid),transparent 65%)}
.section-title{width:1200px;left:0;text-align:center;font-size:39px;font-weight:600;line-height:48px;color:var(--ink)}
.section-text{left:300px;width:600px;text-align:center;font-size:12.5px;line-height:19.5px;color:var(--text)}
.feature{width:200px}
.hex-icon{width:72px;height:82px;clip-path:polygon(50% 0,100% 25%,100% 75%,50% 100%,0 75%,0 25%);background:#222;display:flex;align-items:center;justify-content:center}
.hex-icon.is-orange{background:linear-gradient(160deg,var(--amber),var(--orange-mid))}
.feature h3{margin-top:20px;font-size:16.5px;font-weight:600;line-height:22px;color:var(--ink)}
.feature p{margin-top:11px;font-size:12px;line-height:19px;color:var(--text)}

/* white glove */
.glove-band{left:0;top:1308px;width:1200px;height:800px;clip-path:polygon(0 0,100% 178px,100% 646px,0 798px);background:radial-gradient(ellipse at 900px 250px,#5a5a5a,#2a2a2a 50%,#111 90%)}
.glove-wedge{left:0;top:1950px;width:560px;height:160px;clip-path:polygon(0 0,100% 93px,0 155px);background:var(--grey)}
.glove-title{color:var(--white)}
.service-card{top:1640px;width:256px;height:294px;clip-path:polygon(50% 0,100% 25%,100% 75%,50% 100%,0 75%,0 25%);background:var(--white);text-align:center;padding:48px 30px 0}
.service-card.is-featured{background:linear-gradient(180deg,var(--amber),var(--orange-mid))}
.service-card h3{margin-top:12px;font-size:17px;font-weight:600;color:var(--ink)}
.service-card p{margin-top:8px;font-size:11.5px;line-height:17px;color:var(--text)}
.service-card.is-featured h3,.service-card.is-featured p{color:var(--white)}
.arrow-hex{width:28px;height:32px;margin:20px auto 0;clip-path:polygon(50% 0,100% 25%,100% 75%,50% 100%,0 75%,0 25%);background:var(--ink);display:flex;align-items:center;justify-content:center}
.service-card.is-featured .arrow-hex{background:var(--white)}

/* contact form */
.glow-right{left:640px;top:2050px;width:560px;height:700px;background:radial-gradient(circle at 100% 20%,var(--peach-mid),transparent 65%)}
.form-label{font-size:12px;font-weight:600;color:var(--ink)}
.form-label span{color:var(--orange)}
.field{height:45px;border:1px solid var(--line);background:var(--white);font-size:11px;color:#888;padding:0 20px;display:flex;align-items:center}
.field.textarea{align-items:flex-start;padding-top:14px}
.btn-dark{left:514px;top:2670px;width:173px;height:46px;clip-path:polygon(10% 0,90% 0,100% 50%,90% 100%,10% 100%,0 50%);background:var(--ink);color:var(--white);font-size:11px;font-weight:700;display:flex;align-items:center;justify-content:center}

/* footer */
.footer-bg{left:0;top:2840px;width:1200px;height:655px;clip-path:polygon(0 255px,100% 30px,100% 100%,0 100%);background:#000}
.cta-banner{left:176px;top:2818px;width:848px;height:167px;clip-path:polygon(6% 0,94% 0,100% 50%,94% 100%,6% 100%,0 50%);background:linear-gradient(90deg,var(--orange),var(--amber))}
.cta-title{left:243px;top:2862px;font-size:36px;font-weight:700;color:var(--white)}
.cta-text{left:244px;top:2914px;font-size:12px;color:var(--white)}
.btn-cta{left:780px;top:2880px;width:184px;height:42px;clip-path:polygon(7% 0,93% 0,100% 50%,93% 100%,7% 100%,0 50%);background:var(--white);color:var(--ink);font-size:11px;font-weight:700;display:flex;align-items:center;justify-content:center}
.footer-brand{left:118px;top:3172px;text-align:center;width:194px}
.footer-brand .brand-dot{width:60px;height:60px;margin:0 auto 12px}
.footer-brand .brand-name{color:var(--white);font-size:38px}
.footer-brand .brand-sub{margin:4px 0 0;font-size:13px;letter-spacing:4px;color:#ccc}
.social{top:3305px;width:42px;height:46px;clip-path:polygon(50% 0,100% 25%,100% 75%,50% 100%,0 75%,0 25%);background:#3a3a3a}
.foot-heading{font-family:"Outfit",sans-serif;font-size:17px;font-weight:600;color:var(--white)}
.foot-links{list-style:none;font-size:12px;color:var(--white)}
.foot-links li{height:30px}
.foot-links li::before{content:"» ";color:var(--amber)}
.foot-contact{font-size:12px;line-height:14px;color:var(--white)}
.foot-contact b{font-size:10.5px;display:block;margin-top:16px}
.foot-text{font-size:11.5px;line-height:19px;color:var(--white)}
.news-input{left:792px;top:3245px;width:192px;height:43px;background:var(--white);font-size:11px;color:#888;padding:0 18px;display:flex;align-items:center}
.news-btn{left:984px;top:3245px;width:103px;height:43px;background:linear-gradient(90deg,var(--orange-mid),var(--amber));color:var(--white);font-size:11px;font-weight:700;display:flex;align-items:center;justify-content:center}
.foot-rule{left:112px;top:3432px;width:976px;height:1px;background:#333}
.copyright{left:0;width:1200px;top:3455px;text-align:center;font-size:10.5px;color:var(--white)}
.to-top{left:1124px;top:3388px;width:38px;height:44px;clip-path:polygon(50% 0,100% 25%,100% 75%,50% 100%,0 75%,0 25%);background:linear-gradient(180deg,var(--amber),var(--orange-mid));display:flex;align-items:center;justify-content:center}
</style>
</head>
<body>

<header class="abs site-header">
  <div class="abs brand"><span class="brand-dot"></span><div><span class="brand-name">VARLOWE</span><span class="brand-sub">TECHNOLOGY</span></div></div>
  <nav class="abs main-nav">
    <a class="active">HOME</a><a>CYBERSECURITY</a><a>MANAGED IT</a><a>ABOUT US</a><a>CONTACT</a>
  </nav>
  <svg class="abs search-icon" width="18" height="18" viewBox="0 0 18 18" fill="none" stroke="#111" stroke-width="2"><circle cx="7.5" cy="7.5" r="5.5"/><path d="M11.5 11.5L16 16"/></svg>
  <div class="abs btn-touch">GET IN TOUCH</div>
</header>

<section class="abs hero" role="img" aria-label="Dark digital scene with a glowing padlock over circuitry in amber and orange light"></section>
<p class="abs hero-kicker">Welcome&nbsp; Varlowe Technology</p>
<h1 class="abs hero-title">Enterprise-Level<br><span class="accent">Cybersecurity</span><br>for Every Business</h1>
<p class="abs hero-text">Expert protection, personalized for NGOs, government,<br>and small to mid-sized businesses.</p>
<div class="abs btn-light">REQUEST A FREE CONSULTATION</div>

<div class="abs glow-left"></div>
<h2 class="abs section-title" style="top:838px">Closing the <span class="accent">Security</span> Gap<br>for Mid-Market</h2>
<p class="abs section-text" style="top:950px">In today's digital landscape, every organization, regardless of size, deserves robust protection. We bring the security standards of big business to your doorstep, with a service model that's both accessible and affordable.</p>

<div class="abs feature" style="left:145px;top:1053px">
  <div class="hex-icon"><svg width="32" height="32" viewBox="0 0 32 32" fill="none" stroke="#fff" stroke-width="2"><circle cx="16" cy="11" r="6"/><circle cx="16" cy="11" r="2"/><path d="M5 28v-5h22v5M10 23v5M16 23v5M22 23v5"/></svg></div>
  <h3>Managed<br>SOC</h3>
  <p>24/7/365 monitoring and threat detection for complete peace of mind, without the overhead.</p>
</div>
<div class="abs feature" style="left:384px;top:1053px">
  <div class="hex-icon is-orange"><svg width="32" height="32" viewBox="0 0 32 32" fill="none" stroke="#fff" stroke-width="2"><rect x="7" y="4" width="15" height="22" rx="1"/><path d="M11 10h7M11 15h7M11 20h4"/><circle cx="23" cy="22" r="4"/><path d="M26 25l3 3"/></svg></div>
  <h3>Regulatory<br>Compliance</h3>
  <p>Navigate complex regulations like HIPAA, GDPR, and PCI-DSS with expert guidance and proven solutions.</p>
</div>
<div class="abs feature" style="left:621px;top:1053px">
  <div class="hex-icon"><svg width="32" height="32" viewBox="0 0 32 32" fill="none" stroke="#fff" stroke-width="2"><path d="M16 5l9 4v7c0 6-4 9-9 11-5-2-9-5-9-11V9z"/><path d="M12 16l3 3 5-6"/></svg></div>
  <h3>Pellorin</h3>
  <p style="margin-top:33px">Protect your data with our bespoke multi-layered security framework, built to defend against modern threats.</p>
</div>
<div class="abs feature" style="left:860px;top:1053px">
  <div class="hex-icon"><svg width="32" height="32" viewBox="0 0 32 32" fill="none" stroke="#fff" stroke-width="2"><path d="M16 4l10 4v8c0 6-5 10-10 12-5-2-10-6-10-12V8z"/><rect x="12" y="14" width="8" height="7"/><path d="M13.5 14v-2a2.5 2.5 0 015 0v2"/></svg></div>
  <h3>Vulnerability &amp;<br>Penetration Testing</h3>
  <p>Proactively identify and fix weaknesses before a breach occurs, strengthening your defenses.</p>
</div>

<section class="abs glove-band" role="img" aria-label="Monochrome photo of security specialists working at screens in a data centre"></section>
<div class="abs glove-wedge"></div>
<h2 class="abs section-title glove-title" style="top:1520px">White-Glove <span class="accent">Service,</span><br>Accessible for All.</h2>

<div class="abs service-card" style="left:193px">
  <svg width="48" height="46" viewBox="0 0 48 46"><g fill="#F0912C"><path d="M24 2l2 4 4 .5-3 3 .8 4L24 11.5 20.2 13.5l.8-4-3-3 4-.5z"/><circle cx="14" cy="22" r="5"/><circle cx="34" cy="22" r="5"/><circle cx="24" cy="24" r="6"/><path d="M4 42c0-7 5-12 10-12s10 5 10 12zM24 42c0-7 5-12 10-12s10 5 10 12z"/><path d="M13 44c0-8 5-13 11-13s11 5 11 13z"/></g></svg>
  <h3>Expert Guidance</h3>
  <p>Our experienced NYC and NJ-based team is your partner, not just a vendor.</p>
  <div class="arrow-hex"><svg width="12" height="12" viewBox="0 0 12 12" fill="none" stroke="#fff" stroke-width="1.5"><path d="M2 6h8M7 3l3 3-3 3"/></svg></div>
</div>
<div class="abs service-card is-featured" style="left:469px">
  <svg width="48" height="46" viewBox="0 0 48 46"><path d="M24 3l16 6v11c0 11-7 18-16 22-9-4-16-11-16-22V9z" fill="#fff"/><path d="M17 22l5 5 9-10" fill="none" stroke="#F8CF3A" stroke-width="3"/></svg>
  <h3>Proactive Protection</h3>
  <p>We focus on prevention, not just reaction, to build long-term stability.</p>
  <div class="arrow-hex"><svg width="12" height="12" viewBox="0 0 12 12" fill="none" stroke="#111" stroke-width="1.5"><path d="M2 6h8M7 3l3 3-3 3"/></svg></div>
</div>
<div class="abs service-card" style="left:744px">
  <svg width="48" height="46" viewBox="0 0 48 46"><circle cx="14" cy="16" r="9" fill="#FFC000"/><text x="14" y="21" font-size="13" font-weight="700" text-anchor="middle" fill="#fff" font-family="Poppins,sans-serif">?</text><rect x="22" y="10" width="18" height="30" rx="3" fill="#F0912C"/><circle cx="31" cy="30" r="5" fill="#fff"/><path d="M26 10l5-6 5 6" fill="none" stroke="#EE7325" stroke-width="2"/></svg>
  <h3>Predictable Pricing</h3>
  <p>Achieve enterprise-level security without the enterprise-level price tag.</p>
  <div class="arrow-hex"><svg width="12" height="12" viewBox="0 0 12 12" fill="none" stroke="#fff" stroke-width="1.5"><path d="M2 6h8M7 3l3 3-3 3"/></svg></div>
</div>

<div class="abs glow-right"></div>
<h2 class="abs section-title" style="top:2156px">Ready to <span class="accent">Secure</span><br>Your Future?</h2>
<p class="abs section-text" style="top:2264px">Connect with our team to discuss a tailored plan for your organization's security.</p>

<label class="abs form-label" style="left:240px;top:2311px">Full Name<span>*</span></label>
<div class="abs field" style="left:240px;top:2333px;width:355px">Enter your name</div>
<label class="abs form-label" style="left:608px;top:2311px">Phone<span>*</span></label>
<div class="abs field" style="left:608px;top:2333px;width:355px">Enter your phone</div>
<label class="abs form-label" style="left:240px;top:2391px">Work Email<span>*</span></label>
<div class="abs field" style="left:240px;top:2413px;width:355px">Enter your email</div>
<label class="abs form-label" style="left:608px;top:2391px">Company<span>*</span></label>
<div class="abs field" style="left:608px;top:2413px;width:355px">Enter your company</div>
<label class="abs form-label" style="left:240px;top:2471px">Tell us about your needs...</label>
<div class="abs field textarea" style="left:240px;top:2493px;width:723px;height:140px">Type your message</div>
<div class="abs btn-dark">SEND MESSAGE</div>

<footer>
  <div class="abs footer-bg"></div>
  <div class="abs cta-banner"></div>
  <h2 class="abs cta-title">Ready to Secure Your Future?</h2>
  <p class="abs cta-text">Connect with our team to discuss a tailored plan for your organization's security.</p>
  <div class="abs btn-cta">CONTACT US TODAY</div>

  <div class="abs footer-brand">
    <div class="brand-dot"></div>
    <div class="brand-name">VARLOWE</div>
    <span class="brand-sub">TECHNOLOGY</span>
  </div>
  <div class="abs social" style="left:149px"></div>
  <div class="abs social" style="left:194px"></div>
  <div class="abs social" style="left:239px"></div>

  <h4 class="abs foot-heading" style="left:385px;top:3150px">Useful Links</h4>
  <ul class="abs foot-links" style="left:385px;top:3200px">
    <li>Home</li><li>Cybersecurity</li><li>Managed IT</li><li>About Us</li><li>Contact</li>
  </ul>

  <h4 class="abs foot-heading" style="left:580px;top:3150px">Contact Us</h4>
  <div class="abs foot-contact" style="left:581px;top:3186px">
    <b>PHONE:</b>(555) 014-2290
    <b>EMAIL:</b>info@varlowe-example.com
    <b>LOCATION</b>88 Harbor Ln, New York, NY<br>240 Pier St, Jersey City, NJ
  </div>

  <h4 class="abs foot-heading" style="left:790px;top:3150px">Subscribe to Our Newsletter</h4>
  <p class="abs foot-text" style="left:791px;top:3184px">Get Monthly insights from founders around the<br>globe. No spam-promise.</p>
  <div class="abs news-input">Enter your email</div>
  <div class="abs news-btn">SUBSCRIBE</div>

  <div class="abs foot-rule"></div>
  <p class="abs copyright">© 2025 Varlowe. All rights reserved.</p>
  <div class="abs to-top"><svg width="14" height="14" viewBox="0 0 14 14" fill="none" stroke="#fff" stroke-width="1.6"><path d="M7 12V2M3 6l4-4 4 4"/></svg></div>
</footer>

</body>
</html>
```